EPIC, awesome, creative business card needed - get involved!

I'm launching a boutique, exclusive Property Management real estate agency in Sydney early next year.
The name of the agency will be called "Quartz Hill Lane" - it's a play on "chase the silver pebble trail" to wealth. The Quartz Hill Lane signifies wealth through property investment.
My business will offer management of investment properties (ie Property Management).
The difference with Quartz Hill Lane and other agencies is the business will be run by one of Australia's leading property investment experts, and also one of Australia's leading property managers.
It will be exclusively for high net worth properties and individuals, so the business card needs to be extremely sharp, slick and relatively simple.
The information I want on the card is as follows
Nolan Pryce - Director
M: 0412 967 154
P: 9735 6021
E: nolan@quartzhilllane.net.au
W: quartzhilllane.net.au
I'm happy with the red from the logo, black - no yellows or funky colors. I want this to be a super corporate and slick business card to match the high end nature of the business.
Good luck everyone, and please ask questions for clarification.

```html
<!DOCTYPE html>
<html lang="en">
<head>
<meta charset="utf-8">
<title>Quartz Hill Lane – Business Card</title>
<link rel="stylesheet" href="https://fonts.googleapis.com/css2?family=Source+Sans+3:wght@400;600;700&display=swap">
<style>
  :root {
    --brand-red: #c00000;
    --card-black: #000000;
    --paper-white: #ffffff;
    --line-black: #000000;
  }
  * { box-sizing: border-box; margin: 0; padding: 0; }
  html, body {
    width: 1200px;
    height: 360px;
    overflow: hidden;
    background: var(--paper-white);
    font-family: "Source Sans 3", Arial, sans-serif;
  }
  .sheet {
    position: relative;
    width: 1200px;
    height: 360px;
  }
  .card {
    position: absolute;
    top: 17px;
    width: 554px;
    height: 328px;
  }
  .card--front { left: 17px; background: var(--card-black); }
  .card--back  { left: 629px; background: var(--brand-red); }

  .wordmark {
    position: absolute;
    display: flex;
    align-items: center;
    gap: 12px;
  }
  .wordmark__square {
    width: 26px;
    height: 26px;
    flex: none;
  }
  .wordmark__name {
    color: var(--paper-white);
    font-weight: 600;
    font-size: 30px;
    line-height: 1;
    white-space: nowrap;
  }
  .card--front .wordmark { left: 30px; top: 110px; }
  .card--front .wordmark__square { background: var(--brand-red); }

  .card--back .wordmark {
    left: 0;
    right: 0;
    top: 149px;
    justify-content: center;
  }
  .card--back .wordmark__square { border: 2px solid var(--line-black); }

  .contact {
    position: absolute;
    left: 332px;
    top: 186px;
    color: var(--paper-white);
    font-size: 14px;
    font-weight: 600;
    line-height: 19px;
    list-style: none;
  }
  .contact__name { font-weight: 700; }
  .contact__role { font-size: 10px; font-weight: 700; }
</style>
</head>
<body>
  <main class="sheet">
    <section class="card card--front" aria-label="Card front">
      <div class="wordmark">
        <span class="wordmark__square"></span>
        <p class="wordmark__name">Quartz Hill Lane</p>
      </div>
      <ul class="contact">
        <li><span class="contact__name">Nolan Pryce</span> <span class="contact__role">- Director</span></li>
        <li>M: 0412 967 154</li>
        <li>P: 9735 6021</li>
        <li>E: nolan@quartzhilllane.net.au</li>
        <li>W: quartzhilllane.net.au</li>
      </ul>
    </section>

    <section class="card card--back" aria-label="Card back">
      <div class="wordmark">
        <span class="wordmark__square"></span>
        <p class="wordmark__name">Quartz Hill Lane</p>
      </div>
    </section>
  </main>
</body>
</html>
```